UI Graphics Design For Web Based Home Control

Hi,
Our company Brell Systems is looking for user interface graphics in form of *.psd for home control user interface for a real system which can be used on mobile and PC/MAC.
In Ideal solution, the same interface should be used on mobile, tablets, computers. It changes only to fit the size of the screen. The bigger the screen, the more options you have visible on same view. The user should get familiar interface logic with every device.
The design should have at least the following views covered:
1. Lights view
- List of rooms and lamps
- You can see the status and you can switch it on/off
2. Login view
- Logo (company logo attached)
- Username field
- Password field
3. Dashboard view
- Indicating and choosing home/not home
- Can go to lights view
- Can go to settings view
- Notification list
4. Settings view
- View and edit users
- View and edit lights
Show us your view of ideal home control UI :)
Updates
Time of the project extended by 10 days to receive more designs. If someone sees that the reward should be increased, please also provide the amount expected with the first design. We are willing to increase the amount paid if we see a good design.
Reason: We expect to receive more designs. We are willing to increase the reward if we see good and acceptable designs. Please provide the amount expected with the first design. Project will end with full designs available.
We added our input as an attachment how we see the UI logic. Please have a look into the file.
Reason: We are seeing some good designs. We increased the budget. We are still not where we expect.

```html
<!DOCTYPE html>
<html lang="en">
<head>
<meta charset="utf-8">
<title>Brell Systems – Home Control UI Kit</title>
<link rel="stylesheet" href="https://fonts.googleapis.com/css2?family=Audiowide&display=swap">
<style>
  :root {
    --canvas: #317a9c;
    --header: #ffffff;
    --brand: #0d5a9c;
    --pink: #d42a8c;
    --pink-light: #ec5fb0;
    --pink-dark: #a8186a;
    --cyan: #15a9e6;
    --white: #ffffff;
    --ink: #111111;
    --red: #d3232c;
    --red-light: #f05a4c;
    --orange: #f39a1f;
    --orange-light: #fbc25a;
    --yellow: #f4d61e;
    --yellow-light: #fff07a;
    --ring-dark: #2b2b33;
    --ring-light: #e8e8ee;
  }
  * { box-sizing: border-box; margin: 0; padding: 0; }
  html, body { width: 1200px; height: 918px; overflow: hidden; }
  body {
    position: relative;
    background: var(--canvas);
    font-family: "Audiowide", sans-serif;
  }
  .header {
    position: absolute; left: 14px; top: 33px; width: 1173px; height: 114px;
    background: var(--header);
    display: flex; align-items: center; padding-left: 64px;
  }
  .brand-name {
    font-size: 44px; color: var(--brand); letter-spacing: 1px;
  }
  .dial {
    position: absolute; border-radius: 50%;
    background:
      radial-gradient(circle at 50% 50%, transparent 60%, rgba(0,0,0,.35) 72%, transparent 74%),
      linear-gradient(180deg, var(--ring-dark) 0%, #6a6a74 22%, var(--ring-light) 50%, #8a8a94 78%, var(--ring-dark) 100%);
    box-shadow: 0 0 0 2px #1e1e24;
    display: flex; align-items: center; justify-content: center;
  }
  .dial.large { width: 180px; height: 180px; }
  .dial.medium { width: 100px; height: 100px; }
  .dial.small { width: 82px; height: 82px; }
  .face {
    width: 69%; height: 69%; border-radius: 50%;
    border: 2px solid #3a1a2c;
    display: flex; flex-direction: column; align-items: center; justify-content: center;
    text-align: center; color: var(--white); line-height: 1.1;
    background:
      linear-gradient(180deg, rgba(255,255,255,.35) 0%, rgba(255,255,255,.08) 44%, transparent 46%),
      radial-gradient(circle at 50% 80%, var(--pink-light), var(--pink) 55%, var(--pink-dark));
  }
  .face.light { background: var(--white); color: var(--cyan); }
  .face.red { background: linear-gradient(180deg, rgba(255,255,255,.3) 0%, transparent 46%), radial-gradient(circle at 50% 80%, var(--red-light), var(--red)); }
  .face.orange { background: linear-gradient(180deg, rgba(255,255,255,.3) 0%, transparent 46%), radial-gradient(circle at 50% 80%, var(--orange-light), var(--orange)); }
  .face.yellow { background: linear-gradient(180deg, rgba(255,255,255,.35) 0%, transparent 46%), radial-gradient(circle at 50% 80%, var(--yellow-light), var(--yellow)); color: var(--ink); }
  .large .face { font-size: 21px; }
  .medium .face { font-size: 12px; }
  .small .face { font-size: 11px; }
  .face.list { font-size: 18px; text-align: left; align-items: flex-start; padding-left: 14px; }
  .face .mini-brand { font-size: 22px; color: var(--brand); }
  .bulb { display: block; margin-bottom: 4px; }
  .pill {
    position: absolute; border-radius: 14px; background: var(--white);
    border: 3px solid var(--ink); color: var(--ink);
    display: flex; align-items: center; justify-content: center;
    font-size: 15px;
  }
  .field {
    position: absolute; width: 188px; height: 41px; border-radius: 12px;
    background: var(--white); border: 3px solid var(--cyan);
    display: flex; align-items: center; justify-content: center;
    font-size: 18px; color: var(--ink); letter-spacing: 1px;
  }
  .presence {
    position: absolute; left: 639px; top: 421px; width: 237px; height: 51px;
    border-radius: 18px; background: var(--white); border: 3px solid var(--cyan);
    display: flex; padding: 3px; font-size: 20px;
  }
  .presence span { flex: 1; display: flex; align-items: center; justify-content: center; border-radius: 14px; }
  .presence .off { color: var(--cyan); }
  .presence .on { background: var(--cyan); color: var(--white); }
  .switch {
    position: absolute; width: 82px; height: 26px; border-radius: 12px;
    background: var(--white); border: 2px solid var(--cyan);
    display: flex; padding: 2px; font-size: 13px;
  }
  .switch span { flex: 1; display: flex; align-items: center; justify-content: center; border-radius: 10px; color: var(--ink); }
  .switch .active { background: var(--ink); color: var(--white); }
</style>
</head>
<body>
  <header class="header"><span class="brand-name">Brell Systems</span></header>

  <div class="dial large" style="left:79px;top:199px">
    <div class="face">
      <svg class="bulb" width="28" height="30" viewBox="0 0 28 30" aria-hidden="true">
        <circle cx="14" cy="14" r="13" fill="#222"/>
        <circle cx="14" cy="12" r="7" fill="#f7d21c"/>
        <rect x="10.5" y="18" width="7" height="6" rx="1" fill="#bbb"/>
      </svg>
      Lights<br>view
    </div>
  </div>
  <div class="dial large" style="left:375px;top:199px"><div class="face light">Login<br>view</div></div>
  <div class="dial large" style="left:665px;top:199px"><div class="face" style="font-size:16px">Dashboard<br>view</div></div>
  <div class="dial large" style="left:953px;top:199px"><div class="face" style="font-size:18px">Settings</div></div>
  <div class="dial large" style="left:79px;top:406px"><div class="face list">List of<br>rooms &amp;<br>lights</div></div>
  <div class="dial large" style="left:375px;top:406px"><div class="face light"><span class="mini-brand">Brell</span></div></div>

  <div class="presence"><span class="off">Home</span><span class="on">Not Home</span></div>
  <div class="pill" style="left:918px;top:423px;width:239px;height:51px">View &amp; Edit User</div>
  <div class="pill" style="left:918px;top:497px;width:239px;height:50px">View &amp; Edit Lights</div>

  <div class="dial medium" style="left:709px;top:501px">
    <div class="face">
      <svg class="bulb" width="16" height="17" viewBox="0 0 28 30" aria-hidden="true">
        <circle cx="14" cy="14" r="13" fill="#222"/>
        <circle cx="14" cy="12" r="7" fill="#f7d21c"/>
        <rect x="10.5" y="18" width="7" height="6" rx="1" fill="#bbb"/>
      </svg>
      Lights<br>view
    </div>
  </div>
  <div class="dial medium" style="left:709px;top:620px"><div class="face" style="font-size:10px">Settings</div></div>
  <div class="dial medium" style="left:709px;top:739px"><div class="face" style="font-size:8px">Notification<br>List</div></div>

  <div class="dial small" style="left:47px;top:620px"><div class="face red">living<br>room</div></div>
  <div class="dial small" style="left:153px;top:620px"><div class="face orange">bed<br>room</div></div>
  <div class="dial small" style="left:258px;top:620px"><div class="face yellow" style="font-size:9px">kitchen</div></div>

  <div class="dial small" style="left:47px;top:727px"><div class="face red">6<br>lights</div></div>
  <div class="dial small" style="left:153px;top:727px"><div class="face orange">4<br>lights</div></div>
  <div class="dial small" style="left:258px;top:727px"><div class="face yellow">2<br>lights</div></div>

  <div class="switch" style="left:47px;top:828px"><span>On</span><span class="active">Off</span></div>
  <div class="switch" style="left:153px;top:828px"><span>On</span><span class="active">Off</span></div>
  <div class="switch" style="left:258px;top:828px"><span class="active">On</span><span>Off</span></div>

  <div class="field" style="left:376px;top:631px">username</div>
  <div class="field" style="left:376px;top:682px">password</div>
</body>
</html>
```